RBO Engineering

Client would like a design similar to http://www.movarelq.com/ They will use the product boxes like this site has. My customer's Website is www.rboengineering.com and they are upgrading their KLUND cart to the latest version and mobile friendly. They want to use their corporate colors of blue, white and black. There will be left-hand menu and the top menu. Please let me know if you have any further questions.

This is just for a home page design and inner page/product page design. No coding or installation is involved.
Updates

I apologize to everyone. This client is taking their time going through the designs due to their busy season. Please be patient and we'll get feedback as soon as we can. Thank you, Derek

Industry/Entity Type

Engineering

Number of Pages Required

1 page

Font styles to use
Sans Serif

Requirements
Must have
• Please include an internal product page.

```html
<!DOCTYPE html>
<html lang="en">
<head>
<meta charset="utf-8">
<title>Meridian Sensing Inc. – Specialists in Gas Detection</title>
<link href="https://fonts.googleapis.com/css2?family=Open+Sans:wght@400;600;700&display=swap" rel="stylesheet">
<style>
  :root {
    --blue: #3d6db3;
    --blue-light: #4a8ad0;
    --blue-line: #9cc3e6;
    --green: #8cc63e;
    --ink: #2b2f36;
    --muted: #5a6270;
    --rule: #d3dbe4;
    --page: #ffffff;
    --frame: #8f969e;
  }
  * { box-sizing: border-box; margin: 0; padding: 0; }
  html, body { width: 1200px; height: 1000px; overflow: hidden; }
  body { background: var(--page); font-family: "Open Sans", Arial, sans-serif; color: var(--ink); position: relative; }

  .top-bar { position: absolute; left: 0; top: 0; width: 1200px; height: 72px; border-bottom: 1px solid var(--blue-line); }
  .social { position: absolute; left: 40px; top: 24px; display: flex; gap: 28px; }
  .social-square { width: 22px; height: 22px; background: var(--blue-light); border-radius: 3px; }
  .contact { position: absolute; left: 430px; top: 24px; display: flex; align-items: center; gap: 24px; font-size: 15px; color: var(--blue-light); }
  .contact strong { font-size: 20px; font-weight: 600; margin-left: 4px; }
  .contact-divider { width: 1px; height: 28px; background: var(--blue-line); }

  .cart { position: absolute; right: 60px; top: 0; width: 190px; height: 112px; background: var(--green); display: flex; align-items: center; color: #fff; }
  .cart-icon { width: 62px; height: 100%; display: flex; align-items: center; justify-content: center; border-right: 1px solid rgba(255,255,255,.55); }
  .cart-text { padding: 0 14px; font-size: 14px; line-height: 1.3; }

  .welcome { position: absolute; right: 60px; top: 160px; font-size: 13px; color: var(--ink); }
  .welcome a { color: var(--blue-light); }

  .brand { position: absolute; left: 60px; top: 100px; display: flex; align-items: center; gap: 30px; }
  .brand-name { font-size: 30px; font-weight: 700; color: var(--blue); line-height: 1.05; width: 230px; }
  .brand-tagline { font-size: 17px; font-weight: 700; color: var(--blue); line-height: 1.15; width: 130px; }

  .main-nav { position: absolute; left: 60px; top: 190px; width: 1080px; height: 40px; background: var(--blue); display: flex; align-items: center; padding: 0 14px; }
  .main-nav a { color: #fff; text-decoration: none; font-size: 13px; text-transform: uppercase; letter-spacing: .2px; }
  .main-nav .sep { color: rgba(255,255,255,.7); margin: 0 12px; font-size: 13px; }

  .search { position: absolute; right: 60px; top: 248px; display: flex; }
  .search-field { width: 180px; height: 30px; border: 1px solid var(--blue-line); font-size: 12px; color: #8a929c; padding: 6px 8px; }
  .search-btn { width: 30px; height: 30px; background: var(--blue); display: flex; align-items: center; justify-content: center; }
  .advanced { position: absolute; right: 60px; top: 284px; font-size: 11px; color: var(--blue-light); text-decoration: underline; }

  .sidebar { position: absolute; left: 60px; top: 250px; width: 220px; height: 620px; border-right: 1px solid var(--rule); padding: 70px 20px 0 0; }
  .sidebar h2 { font-size: 20px; font-weight: 600; color: var(--blue-light); margin-bottom: 22px; }
  .sidebar ul { list-style: none; }
  .sidebar li { margin-bottom: 9px; }
  .sidebar li a { font-size: 14px; color: var(--ink); text-decoration: underline; }
  .trust { display: flex; gap: 18px; margin-top: 28px; }
  .made-usa { width: 82px; text-align: center; font-size: 10px; line-height: 1.2; color: var(--ink); }
  .flag { width: 72px; height: 46px; margin: 10px auto 8px; background: linear-gradient(180deg, #b8323a 0%, #f2f2f2 50%, #2e4a8a 100%); }
  .po-card { width: 62px; height: 120px; border: 1px solid var(--rule); background: #fff; text-align: center; padding-top: 8px; font-size: 12px; font-weight: 600; line-height: 1.15; }
  .pay-shape { width: 42px; height: 26px; margin: 8px auto 0; border-radius: 3px; background: #e49a2e; }
  .pay-shape.second { background: #2a4fa0; }
  .secure-badge { margin: 18px 0 0 48px; width: 74px; height: 40px; background: #e6edf5; border-radius: 4px; }

  .content { position: absolute; left: 300px; top: 290px; width: 840px; }
  .content h1 { font-size: 27px; font-weight: 600; color: var(--blue-light); text-align: center; }
  .lede { font-size: 16px; color: var(--muted); text-align: center; width: 620px; margin: 6px auto 0; line-height: 1.35; }

  .products { display: flex; justify-content: center; gap: 60px; margin-top: 50px; }
  .product { text-align: center; }
  .product-photo { width: 150px; height: 190px; border: 6px solid var(--frame); border-radius: 4px; background: linear-gradient(160deg, #3a3f46 0%, #1d2126 100%); }
  .product-name { display: block; margin-top: 12px; font-size: 15px; color: var(--blue-light); }

  .intro { margin: 60px auto 0; width: 780px; font-size: 14px; line-height: 1.55; color: var(--ink); text-align: justify; }
</style>
</head>
<body>

<header class="top-bar">
  <div class="social" aria-label="Social links">
    <span class="social-square"></span>
    <span class="social-square"></span>
    <span class="social-square"></span>
  </div>
  <div class="contact">
    <span>Toll Free: <strong>800-555-0142</strong></span>
    <span class="contact-divider"></span>
    <svg width="22" height="16" viewBox="0 0 22 16" aria-label="Email">
      <rect x="1" y="1" width="20" height="14" fill="none" stroke="#4a8ad0" stroke-width="2"/>
      <path d="M1 1 L11 9 L21 1" fill="none" stroke="#4a8ad0" stroke-width="2"/>
    </svg>
  </div>
</header>

<a class="cart" href="#">
  <span class="cart-icon">
    <svg width="36" height="30" viewBox="0 0 36 30" aria-label="Cart">
      <path d="M2 3 H8 L12 20 H30 L33 8 H10" fill="none" stroke="#fff" stroke-width="2.4" stroke-linejoin="round"/>
      <circle cx="14" cy="26" r="2.5" fill="#fff"/>
      <circle cx="28" cy="26" r="2.5" fill="#fff"/>
    </svg>
  </span>
  <span class="cart-text">Your Cart is Empty now</span>
</a>

<div class="brand">
  <span class="brand-name">Meridian Sensing Inc.</span>
  <span class="brand-tagline">Specialists in Gas Detection</span>
</div>

<p class="welcome">Welcome, Guest! (<a href="#">Register</a> or <a href="#">Login</a>)</p>

<nav class="main-nav">
  <a href="#">Home</a><span class="sep">|</span>
  <a href="#">About</a><span class="sep">|</span>
  <a href="#">Service</a><span class="sep">|</span>
  <a href="#">Products</a><span class="sep">|</span>
  <a href="#">Codes &amp; Design</a><span class="sep">|</span>
  <a href="#">Contact Us</a><span class="sep">|</span>
  <a href="#">Downloads</a><span class="sep">|</span>
  <a href="#">Content</a><span class="sep">|</span>
  <a href="#">My Account</a><span class="sep">|</span>
  <a href="#">Portable Gas Detector Calibrations</a>
</nav>

<div class="search">
  <span class="search-field">Search this site</span>
  <span class="search-btn">
    <svg width="14" height="14" viewBox="0 0 14 14" aria-label="Search">
      <circle cx="6" cy="6" r="4.5" fill="none" stroke="#fff" stroke-width="1.8"/>
      <path d="M9.5 9.5 L13 13" stroke="#fff" stroke-width="1.8"/>
    </svg>
  </span>
</div>
<a class="advanced" href="#">advanced search</a>

<aside class="sidebar">
  <h2>Products</h2>
  <ul>
    <li><a href="#">Controllers</a></li>
    <li><a href="#">Fixed Gas Detection</a></li>
    <li><a href="#">Calibration Gas</a></li>
    <li><a href="#">Replacement (sensors/cells)</a></li>
    <li><a href="#">Accessories</a></li>
    <li><a href="#">Portable Gas Detections</a></li>
  </ul>
  <div class="trust">
    <div class="made-usa">
      <div class="flag" role="img" aria-label="Flag of the United States"></div>
      Our products are proudly made in the USA
    </div>
    <div class="po-card">
      Purchase<br>Order
      <div class="pay-shape"></div>
      <div class="pay-shape second"></div>
    </div>
  </div>
  <div class="secure-badge"></div>
</aside>

<main class="content">
  <h1>Specialists in Ammonia Gas Detection</h1>
  <p class="lede">New - Two (2) year warranty on all AirSentry sensing elements and transmitters. Includes NH3 sensors, CO2 sensors, and R22 sensors among others.</p>

  <div class="products">
    <a class="product" href="#">
      <div class="product-photo" role="img" aria-label="NH3 sensor enclosure photo"></div>
      <span class="product-name">NH3 Sensors</span>
    </a>
    <a class="product" href="#">
      <div class="product-photo" role="img" aria-label="CO2 sensor enclosure photo"></div>
      <span class="product-name">CO2 Sensors</span>
    </a>
    <a class="product" href="#">
      <div class="product-photo" role="img" aria-label="R22 sensor enclosure photo"></div>
      <span class="product-name">R22 Sensors</span>
    </a>
  </div>

  <p class="intro">Ammonia gas detection may not be your company's core business. At Meridian Sensing, ammonia gas detection, protection of your personnel, and protection of your assets is our business. Let us help you design and maintain your ammonia gas detection system. We specialize in innovative safety-system solutions for cold storage facilities, food processing areas, refrigeration systems, compressor rooms, tank rooms, heat treatment facilities, breweries, refineries and more. Our technical savvy staff is highly capable of assisting you with your applications.</p>
</main>

</body>
</html>
```